Airborne Sensor Mfr Needs New Backdrop for Exhibition Booth

Our company manufacturers airborne hyperspectral and thermal cameras installed on drones and aircraft. Our customers work in numerous fields from forestry to oceanography, and from defense to oil & gas. We will be attending an airborne survey and mapping conference in a few months and want to try a new backdrop for the booth which will be about 3m x 3m. We are looking for something new and fresh with a high-tech but simple feel, professional and established but also friendly and inviting. Please see my below primitive draft design for some suggested text, images, and icons that I have in mind. Can you turn this into something really compelling that draws people to our booth? Or do you have some new ideas to build on my design? Look forward to seeing what you can do!
https://pelvaq.com/

```html
<!DOCTYPE html>
<html lang="en">
<head>
<meta charset="utf-8">
<title>PELVAQ Airborne Sensors Backdrop</title>
<link href="https://fonts.googleapis.com/css2?family=Poppins:wght@400;500;600;700;800&display=swap" rel="stylesheet">
<style>
  :root {
    --page-bg: #dfe5ee;
    --ink: #111111;
    --teal: #2fb8c6;
    --indigo: #3a3a9e;
    --purple: #8a3aa6;
    --magenta: #d93a8c;
    --red: #ee3a3a;
    --orange: #f39a2b;
    --sky-top: #9fcdf2;
    --sky-mid: #e3eef8;
    --mist: #f2f3f5;
    --rule: #8a3aa6;
    --dash: #5ab8d8;
  }
  * { margin: 0; padding: 0; box-sizing: border-box; }
  html, body { width: 721px; height: 1200px; overflow: hidden; background: var(--page-bg); font-family: "Poppins", sans-serif; color: var(--ink); }
  .backdrop {
    position: absolute; left: 10px; top: 250px; width: 700px; height: 700px; overflow: hidden;
    background: linear-gradient(180deg, var(--sky-top) 0%, var(--sky-mid) 35%, var(--mist) 60%, #ececef 100%);
    box-shadow: 0 6px 24px rgba(0,0,0,.12);
  }
  .photo { position: absolute; }
  .photo-aircraft { left: 370px; top: 18px; width: 330px; height: 180px; border-radius: 40% 10% 30% 50%; background: linear-gradient(160deg, #f4f6f8 0%, #cfd6dd 55%, #9bd36a 100%); opacity: .85; }
  .photo-sensor-pod { left: 495px; top: 200px; width: 150px; height: 120px; background: linear-gradient(90deg, #b8282a 0%, #b8282a 50%, #2e2e30 50%, #2e2e30 100%); border-radius: 4px; }
  .photo-camera { left: 42px; top: 545px; width: 150px; height: 140px; background: radial-gradient(circle at 60% 45%, #3a4a42 0 12%, #1e1f22 13% 100%); border-radius: 10px; }
  .brand { position: absolute; left: 62px; top: 68px; font-weight: 800; font-size: 48px; letter-spacing: 1px; color: var(--ink); line-height: 1; }
  .headline-top { position: absolute; left: 26px; top: 160px; font-weight: 800; font-size: 58px; line-height: 1; }
  .headline-main {
    position: absolute; left: 24px; top: 212px; font-weight: 800; font-size: 80px; line-height: 1;
    background: linear-gradient(90deg, var(--teal) 0%, var(--indigo) 25%, var(--purple) 45%, var(--magenta) 65%, var(--red) 82%, var(--orange) 100%);
    -webkit-background-clip: text; background-clip: text; color: transparent;
  }
  .question { position: absolute; left: 28px; top: 310px; font-weight: 800; font-size: 24px; line-height: 1.3; }
  .frame { position: absolute; left: 0; top: 0; width: 700px; height: 700px; }
  .use { position: absolute; width: 90px; text-align: center; font-size: 9px; font-weight: 500; line-height: 1.2; }
  .ring { width: 36px; height: 36px; margin: 0 auto 6px; border-radius: 50%; padding: 3px;
    background: linear-gradient(135deg, var(--purple), var(--magenta), var(--orange)); }
  .ring span { display: block; width: 100%; height: 100%; border-radius: 50%; background: #fff; position: relative; }
  .ring span::after { content: ""; position: absolute; left: 50%; top: 50%; width: 12px; height: 12px; margin: -6px 0 0 -6px; border: 1.5px solid var(--magenta); border-radius: 50%; }
  .visit { position: absolute; left: 257px; top: 568px; font-weight: 600; font-size: 17px; }
  .url { position: absolute; left: 256px; top: 586px; font-weight: 700; font-size: 35px; letter-spacing: .5px; }
  .url .domain { color: var(--magenta); }
</style>
</head>
<body>
<main class="backdrop">
  <div class="photo photo-aircraft" role="img" aria-label="Photo of a passenger jet climbing through a cloudy sky"></div>
  <div class="photo photo-sensor-pod" role="img" aria-label="Photo of a red airborne sensor unit with black mounting frame"></div>

  <svg class="frame" viewBox="0 0 700 700" aria-hidden="true">
    <defs>
      <linearGradient id="swoosh" x1="0" y1="0" x2="1" y2="0">
        <stop offset="0" stop-color="#2fb8c6"/><stop offset=".3" stop-color="#3a3a9e"/>
        <stop offset=".55" stop-color="#d93a8c"/><stop offset=".8" stop-color="#ee3a3a"/>
        <stop offset="1" stop-color="#f39a2b"/>
      </linearGradient>
    </defs>
    <path d="M0 522 C140 590 420 650 700 610 L700 700 L0 700 Z" fill="url(#swoosh)"/>
    <path d="M0 540 C160 610 420 640 700 600 L700 612 C420 655 160 630 0 560 Z" fill="#ffffff"/>
    <path d="M340 652 C480 660 600 650 700 630 L700 640 C600 662 480 668 340 652 Z" fill="#ffffff"/>
    <path d="M385 350 H665 Q675 350 675 360 V545 Q675 555 665 555 H248" fill="none" stroke="var(--rule)" stroke-width="1.5"/>
    <path d="M593 350 H665 Q675 350 675 360 V432 Z" fill="var(--purple)"/>
    <circle cx="246" cy="555" r="3.5" fill="#fff" stroke="var(--rule)" stroke-width="1.5"/>
    <g stroke="#d0d3d8" stroke-width="1">
      <line x1="120" y1="378" x2="120" y2="530"/><line x1="204" y1="378" x2="204" y2="530"/>
      <line x1="290" y1="378" x2="290" y2="530"/><line x1="376" y1="378" x2="376" y2="530"/>
      <line x1="472" y1="378" x2="472" y2="530"/><line x1="568" y1="378" x2="568" y2="530"/>
    </g>
    <g stroke="var(--dash)" stroke-width="1" stroke-dasharray="3 2">
      <line x1="135" y1="451" x2="192" y2="451"/><line x1="220" y1="451" x2="276" y2="451"/>
      <line x1="305" y1="451" x2="362" y2="451"/><line x1="397" y1="451" x2="454" y2="451"/>
      <line x1="490" y1="451" x2="547" y2="451"/>
    </g>
  </svg>

  <div class="brand">PELVAQ</div>
  <h1 class="headline-top">AIRBORNE</h1>
  <h2 class="headline-main">SENSORS</h2>
  <p class="question">WHAT DO YOU WANT<br>TO DETECT AND MONITOR?</p>

  <div class="use" style="left:30px;top:419px"><div class="ring"><span></span></div>Gas<br>Detection</div>
  <div class="use" style="left:117px;top:374px"><div class="ring"><span></span></div>Forestry</div>
  <div class="use" style="left:202px;top:374px"><div class="ring"><span></span></div>Water<br>Quality</div>
  <div class="use" style="left:288px;top:374px"><div class="ring"><span></span></div>Vegetation</div>
  <div class="use" style="left:380px;top:374px"><div class="ring"><span></span></div>Health<br>Precision Ag</div>
  <div class="use" style="left:473px;top:374px"><div class="ring"><span></span></div>Species<br>Classification</div>
  <div class="use" style="left:571px;top:420px"><div class="ring"><span></span></div>Pollution<br>/ Disaster<br>Response</div>
  <div class="use" style="left:117px;top:462px"><div class="ring"><span></span></div>Target<br>Detection</div>
  <div class="use" style="left:202px;top:462px"><div class="ring"><span></span></div>Environmental<br>Monitoring</div>
  <div class="use" style="left:288px;top:462px"><div class="ring"><span></span></div>Geology<br>/ Mineral<br>Exploration</div>
  <div class="use" style="left:380px;top:462px"><div class="ring"><span></span></div>Thermal<br>Anomalies</div>
  <div class="use" style="left:473px;top:462px"><div class="ring"><span></span></div>Wildfire /<br>Hotspot</div>

  <div class="photo photo-camera" role="img" aria-label="Photo of a black thermal imaging camera with a round lens"></div>

  <p class="visit">Visit us at</p>
  <p class="url">www.<span class="domain">pelvaq</span>.com</p>
</main>
</body>
</html>
```